Web Design Project for a Software & Consulting Company

We have just completed a recent ArtFlock project for a new logo (see attached).
As the next stage of our rebranding we now require a website re-design to complement the new logo.
Our current site, http://www.rigsumsoft.example was built in-house and does not come across as professional as we would like. We supply software and associated services to some of the world’s largest oil companies and we need our site to reflect that level of client.
We will also be posting another design project for brochures, PowerPoint slides and other materials very soon.
We would like designs for…
Home page
Product page
• QTV
• BLZ
• FNQ
Services
News page
About Us page
Contact Us page
Page for mobile devices that gives basic company and product information
Currently the site is small but we intend to increase content to include white papers etc. this should be taken into account when designing the navigation therefore we would prefer navigation through styled text links rather than images.
Colour schemes should broadly be taken from our new logo, where the dark blue and dark green from the left and right sides of the logo are the main colours, but other, brighter accent colours can be used to highlight sections or content.
Dark Blue = C:88, M:55, Y:44, K:28
Dark Green = C:87, M:53, Y:50, K:50
NB: Don’t use the logo on our current site, make sure you use the one attached.
We would prefer the final file format to be a layered PSD.
The site should be clean and professional and communicate the following...
• That we have a great depth and breadth of knowledge about our customers’ business, enabling us to deliver the best systems and solutions.
• That we are a leading provider of cost estimation and control solutions to the oil and gas industry.
• The benefits of our software and consulting services.
• Show that we deliver outstanding customer service and value with a very high level of professionalism
• The site should have no Flash and be able to self-adjust to fit any screen size.
Things to avoid …
• Obvious and clichéd oil industry imagery, no oil rigs
• Cartoon style graphics
Our Background
We are an integrated software and consulting organization specialising in the drilling side of the oil and gas industry. Simply put our software helps companies better understand, predict and communicate the cost of drilling wells.
We have 3 software products and a consulting offering consisting of…
• QTV - Probabilistic time and cost software
• BLZ – Cost tracking and reporting software
• FNQ – (currently known as BoreMemory) – Lessons learned software
• Consulting services
Our systems are in use in over 30 countries with a broad range of clients including: GN, Solvane, Prue, Tolmar, VONI Kelstra, SALVEM and Quorlit.
Our current site can be found at www.rigsumsoft.example
Our main competitors are
• http://www.gavondel.example/
• http://www.mirrowen.example/
• http://www.tbx.example/services/software-solutions/p1-
Our depth of drilling knowledge, quality of software and collaboration with clients differentiate us form the competition.
We strive for very high levels of customer service.
We look forward to receiving your designs!
Updates
Thanks to all the designers who have submitted a design, we appreciate the effort.
We will do our best to give individual feedback on each design but given that many are quite similar we thought we would give some general feedback first.
Nearly all the designs submitted so far have been slight variations on…
-
Top Menu
-
Scrolling Photo Banner
-
4 Columns
-
Body
-
Deep Footer
These designs are well executed but they are basically the same layout as our existing site and while there is nothing inherently wrong with this layout we would like to see some designs that are a bit more innovative and different. We don’t really want just a polished version of our current site.
Thanks again,
RST
Thanks to everyone who has submitted a design, the response has been great.
We are close to making a decision so if you are intending to submit a design please do it soon, the deadline is only a few days away.
Thanks again.
RST
Target Market(s)
Mid to high level executives
Industry/Entity Type
Oil And Gas
Look and feel

```html
<!DOCTYPE html>
<html lang="en">
<head>
<meta charset="utf-8">
<title>Rigsum Soft Technologies – FNQ</title>
<link rel="stylesheet" href="https://fonts.googleapis.com/css2?family=Arimo:wght@400;700&family=PT+Sans:wght@400;700&family=PT+Sans+Narrow&display=swap">
<style>
:root{
  --teal-dark:#1d4f5f;
  --teal-head:#1b5265;
  --link:#1a8db0;
  --text:#4a4a4a;
  --rule:#cfcfcf;
  --white:#ffffff;
  --banner-deep:#1f5a7c;
  --banner-light:#cfe3ee;
}
*{box-sizing:border-box;margin:0;padding:0}
html,body{width:952px;height:1200px;overflow:hidden;background:var(--white)}
body{position:relative;font-family:"Arimo",Arial,sans-serif;color:var(--text)}
.abs{position:absolute}

/* header */
.brand{left:116px;top:38px;display:flex;align-items:center;gap:8px;font-family:"PT Sans",sans-serif;font-weight:700;font-size:19px;color:var(--teal-dark);letter-spacing:.5px}
.brand-dot{width:28px;height:28px;border-radius:50%;background:var(--teal-dark)}
.main-nav{left:0;top:56px;width:952px;height:24px;font-family:"PT Sans Narrow",sans-serif;font-size:12px;color:#222}
.main-nav a{position:absolute;top:5px;color:#222;text-decoration:none}
.main-nav a.active{top:0;height:24px;line-height:24px;padding:0 8px;background:var(--teal-dark);color:var(--white);border-radius:3px;border:1px solid #0e2f3a}

/* banner */
.hero{left:94px;top:129px;width:762px;height:238px;background:linear-gradient(100deg,var(--banner-deep) 0%,#3b7fa6 40%,#a9cde0 62%,var(--banner-light) 100%)}
.hero-caption{left:0;top:164px;width:762px;height:51px;background:rgba(16,58,74,.88);font-family:"PT Sans",sans-serif;font-weight:700;font-size:22px;color:var(--white);line-height:51px;padding-left:28px}
.hero-base{left:0;top:215px;width:762px;height:23px;background:linear-gradient(#b9cfdc,#e8f0f5)}

/* intro */
.intro-icon{left:96px;top:399px;width:36px;height:27px;background:#6fae7b;border:3px solid #c9a27a;transform:rotate(-8deg)}
.intro-title{left:144px;top:402px;font-family:"PT Sans",sans-serif;font-size:18px;color:var(--teal-head)}
.intro-text{left:96px;top:447px;width:735px;font-size:10px;line-height:14.4px}
.intro-text p{margin-bottom:22px}

/* features */
.section-title{font-family:"PT Sans",sans-serif;font-size:16.5px;color:var(--teal-head)}
.rule{height:2px;background:var(--rule)}
.feature-icon{width:38px;height:36px;border-radius:6px}
.feature-title{font-size:9.6px;font-weight:700;color:#111}
.feature-text{width:160px;font-size:9.6px;line-height:16px;color:var(--text);margin-top:3px}
.read-more{display:flex;align-items:center;gap:6px;font-size:9px;font-weight:700;color:var(--link)}
.read-more i{width:10px;height:10px;border-radius:50%;background:#444;position:relative;display:inline-block}
.read-more i::before,.read-more i::after{content:"";position:absolute;background:#fff;left:2px;top:4px;width:6px;height:2px}
.read-more i::after{transform:rotate(90deg)}
.shot{width:82px;height:82px;border:1px solid #dcdcdc;padding:3px;background:#f3f3f3}
.shot span{display:block;width:100%;height:100%}

/* footer */
.site-footer{left:94px;top:969px;width:762px;height:231px;background:var(--teal-dark);color:#e8eef0}
.foot-head{font-family:"PT Sans Narrow",sans-serif;font-size:13px;color:var(--white);padding-bottom:4px;border-bottom:1px solid #4b7582;width:117px}
.foot-text{font-family:"PT Sans Narrow",sans-serif;font-size:10.5px;line-height:13.6px;margin-top:5px}
.badge{width:178px;height:44px;border-radius:4px;background:#2e6574}
.touch{font-family:"PT Sans",sans-serif;font-size:15.5px;color:var(--white)}
.touch-line{height:1px;width:140px;background:linear-gradient(90deg,#4fb4cf,transparent);margin-top:4px}
.field{left:578px;width:158px;background:var(--white);border:1px solid #aab;border-radius:2px;font-family:"PT Sans",sans-serif;font-size:10px;color:#333;padding:4px 8px}
.submit{left:685px;top:165px;width:51px;height:19px;background:linear-gradient(#fff,#ddd);border:1px solid #999;font-size:8px;font-weight:700;color:#222;text-align:center;line-height:17px}
.foot-lorem{left:22px;top:132px;width:530px;font-size:9.4px;line-height:11.6px}
.foot-bottom{left:0;top:199px;width:762px;height:1px;background:#153d49}
.foot-links{left:22px;top:210px;font-size:8.4px}
.copy{right:26px;top:210px;font-size:8.4px}
</style>
</head>
<body>

<header>
  <div class="abs brand"><span class="brand-dot"></span>RIGSUM SOFT TECHNOLOGIES</div>
  <nav class="abs main-nav">
    <a style="left:424px" href="#">HOME</a>
    <a class="active" style="left:481px" href="#">PRODUCTS</a>
    <a style="left:574px" href="#">SERVICES</a>
    <a style="left:652px" href="#">NEWS</a>
    <a style="left:713px" href="#">ABOUT US</a>
    <a style="left:790px" href="#">CONTACT US</a>
  </nav>
</header>

<section class="abs hero" role="img" aria-label="Photo of hands typing on a laptop beneath a world map with connected business people silhouettes">
  <div class="abs hero-base"></div>
  <div class="abs hero-caption">FNQ - Lessons learned software</div>
</section>

<section>
  <div class="abs intro-icon" role="img" aria-label="Small green chalkboard icon"></div>
  <h1 class="abs intro-title" style="font-weight:400">THE BEST SOFTWARE TO LEARNED LESSONS</h1>
  <div class="abs intro-text">
    <p>Plusieurs variations de Lorem Ipsum peuvent être trouvées ici ou là, mais la majeure partie d'entre elles a été altérée par l'addition d'humour ou de mots aléatoires qui ne ressemblent pas une seconde à du texte standard. Si vous voulez utiliser un passage du Lorem Ipsum.</p>
    <p>Vous devez être sûr qu'il n'y a rien d'embarrassant caché dans le texte. Tous les générateurs de Lorem Ipsum sur Internet tendent à reproduire le même extrait sans fin, ce qui fait de loremtext.example le seul vrai générateur de Lorem Ipsum.</p>
    <p>Iil utilise un dictionnaire de plus de 200 mots latins, en combinaison de plusieurs structures de phrases, pour générer un Lorem Ipsum irréprochable. Le Lorem Ipsum ainsi obtenu ne contient aucune répétition, ni ne contient des mots farfelus, ou des touches d'humour.</p>
  </div>
</section>

<section>
  <h2 class="abs section-title" style="left:115px;top:636px;font-weight:400">MAIN FEATURES</h2>
  <div class="abs rule" style="left:96px;top:667px;width:430px"></div>

  <div class="abs feature-icon" style="left:106px;top:695px;background:linear-gradient(#e0b060,#a86c26)" role="img" aria-label="Software box with disc icon"></div>
  <div class="abs" style="left:158px;top:694px">
    <div class="feature-title">L'extrait standard de Lorem</div>
    <div class="feature-text">On sait depuis longtemps que travailler avec du texte lisible et contenant du sens est source de distractions, et empêche de se concentrer.</div>
  </div>
  <a class="abs read-more" style="left:221px;top:805px"><i></i>Read More</a>

  <div class="abs feature-icon" style="left:325px;top:695px;background:linear-gradient(#5a8fe0,#1f4fb0)" role="img" aria-label="Stacked windows icon"></div>
  <div class="abs" style="left:376px;top:694px">
    <div class="feature-title">Fait de loremtext.example le seul vrai</div>
    <div class="feature-text">Plusieurs variations de Lorem Ipsum peuvent être trouvées ici ou là, mais la majeure partie d'entre elles a été altérée par l'addition d'humour ou de mots aléatoires qui.</div>
  </div>
  <a class="abs read-more" style="left:446px;top:805px"><i></i>Read More</a>

  <svg class="abs" style="left:107px;top:836px" width="36" height="36" viewBox="0 0 36 36" role="img" aria-label="Refresh icon">
    <circle cx="18" cy="18" r="17" fill="#f0863a"/>
    <path d="M9 17a9 9 0 0 1 16-5" stroke="#fff" stroke-width="3" fill="none"/>
    <path d="M27 19a9 9 0 0 1-16 5" stroke="#fff" stroke-width="3" fill="none"/>
    <path d="M26 6v7h-7z" fill="#fff"/><path d="M10 30v-7h7z" fill="#fff"/>
  </svg>
  <div class="abs" style="left:158px;top:839px">
    <div class="feature-title">Plusieurs versions sont app</div>
    <div class="feature-text">Have evolved over the years, sometimes by accident, some-times on purpose.</div>
  </div>
  <a class="abs read-more" style="left:221px;top:919px"><i></i>Read More</a>

  <div class="abs feature-icon" style="left:326px;top:836px;background:#2f7a3c;border:3px solid #9a6a3a" role="img" aria-label="Chalkboard on easel icon"></div>
  <div class="abs" style="left:376px;top:839px">
    <div class="feature-title">De Finibus Bonorum et Mal</div>
    <div class="feature-text">Belief, Lorem Ipsum is not simply random text It has roots in a.piece of classical Latin .</div>
  </div>
  <a class="abs read-more" style="left:445px;top:919px"><i></i>Read More</a>

  <h2 class="abs section-title" style="left:571px;top:636px;font-weight:400">SOFTWARE FEATURES</h2>
  <div class="abs rule" style="left:549px;top:667px;width:306px"></div>

  <div class="abs shot" style="left:570px;top:691px"><span role="img" aria-label="Software screenshot" style="background:linear-gradient(#dfe6ea,#9bbf6a 55%,#e8edf0)"></span></div>
  <div class="abs shot" style="left:658px;top:691px"><span role="img" aria-label="Software screenshot" style="background:linear-gradient(#1f6b3a,#e5e5e5 35%,#d8d8d8 70%,#1f6b3a)"></span></div>
  <div class="abs shot" style="left:746px;top:691px"><span role="img" aria-label="Software screenshot" style="background:linear-gradient(#e8e8ec,#6b8fd8 50%,#eef0f4)"></span></div>
  <div class="abs shot" style="left:570px;top:780px"><span role="img" aria-label="Software screenshot" style="background:linear-gradient(#f4f4f4,#e6d3dc 50%,#f0f0f0)"></span></div>
  <div class="abs shot" style="left:658px;top:780px"><span role="img" aria-label="Software screenshot with pie chart" style="background:radial-gradient(circle at 55% 60%,#d9733a 0 18%,#3a78b0 19% 28%,#5a6a74 29%)"></span></div>
  <div class="abs shot" style="left:746px;top:780px"><span role="img" aria-label="Software screenshot with bar chart" style="background:linear-gradient(90deg,#c9d8e6,#f2f4f6 45%,#2a3f9a 70%,#f2f4f6)"></span></div>

  <a class="abs read-more" style="left:738px;top:877px"><i></i>view all products</a>
</section>

<footer class="abs site-footer">
  <div class="abs" style="left:24px;top:22px">
    <div class="foot-head">EUROPE</div>
    <div class="foot-text">12 Harlow Row<br>Dunmere, DN4 2QT<br>Phone:+44(0)1632 960418<br>Email:eu@rigsumsoft.example</div>
  </div>
  <div class="abs" style="left:184px;top:22px">
    <div class="foot-head">NORTH AMERICA</div>
    <div class="foot-text">4100 Larkfield Ave, Suite 210<br>Brenton, TX 77990<br>Phone:(555) 014 7720<br>Email:us@rigsumsoft.example</div>
  </div>
  <div class="abs" style="left:360px;top:22px">
    <div class="foot-head" style="width:178px">OUR GOLD BUSINESS PARTNER</div>
    <div class="badge" style="margin-top:12px"></div>
  </div>
  <div class="abs" style="left:578px;top:16px">
    <div class="touch">Get in touch</div>
    <div class="touch-line"></div>
  </div>
  <div class="abs field" style="top:51px;height:21px">Name</div>
  <div class="abs field" style="top:79px;height:21px">E-mail</div>
  <div class="abs field" style="top:107px;height:50px">Message</div>
  <div class="abs submit">SUBMIT</div>

  <div class="abs" style="left:22px;top:115px;width:528px;height:1px;background:#4b7582"></div>
  <p class="abs foot-lorem">Lorem ipsum dolor sit amet, consectetur adipiscing elit. Donec semper nisl eget ante vehicula at viverra est porta. Morbi eleifend, turpis eget vehicula porta, leo velit facilisis justo, quis vehicula velit erat nec est. Pellentesque habitant morbi tristique senectus et netus et malesuada fames ac turpis egestas. Pellentesque consequat est vel metus luctus commodo. In hac habitasse platea dictumst. Suspendisse justo ipsum,</p>
  <div class="abs foot-bottom"></div>
  <div class="abs foot-links">Privacy Policy &nbsp;&nbsp;|&nbsp;&nbsp; Terms &amp; Conditions</div>
  <div class="abs copy">© Copyrights 2012 Rigsum Soft</div>
</footer>

</body>
</html>
```